Thriving Through Slimming Book Cover

I need an eBook cover for my book
Title: Thriving Through Slimming - Steer Your Thoughts, Shape Your Frame
Subtitle: Bid Farewell to Seesaw Eating and Welcome Decades of Vigor and Joy
Author: Martin Kessler

This book is about learning the mechanisms behind weight loss and how to cultivate two qualities: discipline and consistency

Weight Loss, Mind Hack

• I would like to see 2 images of the same woman standing back to back. The one on the left is overweight and sad and the one on the right is not overweight and smiling.

```html
<!DOCTYPE html>
<html lang="en">
<head>
<meta charset="utf-8">
<title>Thriving Through Slimming – Book Cover</title>
<link rel="stylesheet" href="https://fonts.googleapis.com/css2?family=Bebas+Neue&display=swap">
<style>
  :root {
    --page: #ffffff;
    --cover: #fd7777;
    --ink: #323d59;
    --light: #ffffff;
    --art-top: #f7b2a3;
    --art-bottom: #3b4662;
  }
  html, body {
    margin: 0;
    padding: 0;
    width: 1200px;
    height: 1200px;
    overflow: hidden;
    background: var(--page);
  }
  .canvas {
    display: block;
    width: 1200px;
    height: 1200px;
  }
  .cover-bg { fill: var(--cover); }
  .type { font-family: "Bebas Neue", "Oswald", sans-serif; text-anchor: middle; }
  .ink { fill: var(--ink); }
  .light { fill: var(--light); }
</style>
</head>
<body>
<svg class="canvas" viewBox="0 0 1200 1200" xmlns="http://www.w3.org/2000/svg">
  <defs>
    <linearGradient id="art-fill" x1="0" y1="0" x2="0" y2="1">
      <stop offset="0" stop-color="var(--art-top)"/>
      <stop offset="1" stop-color="var(--art-bottom)"/>
    </linearGradient>
  </defs>

  <g class="book-cover">
    <rect class="cover-bg" x="289" y="132" width="629" height="943"/>

    <text class="type ink title-main" x="604" y="322" font-size="186"
          textLength="470" lengthAdjust="spacingAndGlyphs">THRIVING</text>

    <text class="type light title-sub" x="604" y="406" font-size="91"
          textLength="432" lengthAdjust="spacingAndGlyphs">THROUGH SLIMMING</text>

    <text class="type tagline" x="606" y="473" font-size="59"
          textLength="430" lengthAdjust="spacingAndGlyphs"><tspan class="ink">STEER</tspan><tspan class="light"> YOUR THOUGHTS</tspan></text>
    <text class="type tagline" x="606" y="522" font-size="59"
          textLength="430" lengthAdjust="spacing"><tspan class="ink">SHAPE</tspan><tspan class="light"> YOUR FRAME</tspan></text>

    <rect class="cover-art" x="475" y="537" width="325" height="379" rx="24"
          fill="url(#art-fill)" opacity="0.55" role="img"
          aria-label="Illustration of the same woman shown twice back to back: on the left overweight and downcast, on the right slim in a navy dress with a measuring tape around her waist"/>

    <text class="type ink subtitle" x="603" y="967" font-size="29"
          textLength="290" lengthAdjust="spacingAndGlyphs">BID FAREWELL TO SEESAW EATING</text>
    <text class="type ink subtitle" x="603" y="995" font-size="29"
          textLength="462" lengthAdjust="spacingAndGlyphs">AND WELCOME DECADES OF VIGOR AND JOY</text>

    <text class="type light author" x="603" y="1053" font-size="46"
          textLength="317" lengthAdjust="spacingAndGlyphs">MARTIN KESSLER</text>
  </g>
</svg>
</body>
</html>
```